Swimming Pool Supply Company Business Cards

We need business cards designed for company. These need to be easy to edit so that we can fill in names, titles, and contact info for each person who works here.

Dalton R. Whitfield
Manager of Legal & Finance
K.L. Brisbane, Incorporated

4837 Grenway Avenue
Marlow Heights, PA 19243

E. dalton@klbrisbane-example.com
M. (215) 555-0173
O. (215) 555-0148

Contact Information for Business Card

Looking to upgrade current business cards with graphic that can be edited. Looking for fresh ideas for an age old industry.

Font styles to use
Serif
Sans Serif

Colors

Designer to choose colors to be used in the design.

Requirements
Must have
• Professional, fresh, unique but professional

```html
<!DOCTYPE html>
<html lang="en">
<head>
<meta charset="utf-8">
<title>K.L. Brisbane Business Cards</title>
<link rel="stylesheet" href="https://fonts.googleapis.com/css2?family=Raleway:wght@600;700&family=Lato:wght@400;700&display=swap">
<style>
  :root {
    --backdrop: #48484a;
    --navy: #25235c;
    --ink: #2b2b33;
    --blue: #1a5aa6;
    --blue-deep: #144d92;
    --pool-top: #2f2b6a;
    --pool-bottom: #3b3680;
    --paper: #ffffff;
    --paper-shade: #e9e9ec;
  }
  html, body {
    margin: 0;
    width: 1200px;
    height: 1200px;
    overflow: hidden;
    background: var(--backdrop);
  }
  .canvas {
    position: relative;
    width: 1200px;
    height: 1200px;
  }
  .card {
    position: absolute;
    left: 120px;
    width: 960px;
    height: 549px;
    overflow: hidden;
    box-shadow: 0 10px 30px rgba(0,0,0,0.35);
  }

  /* Back of card */
  .card-back { top: 40px; }
  .pool-photo {
    position: absolute;
    inset: 0;
    background: radial-gradient(ellipse at 55% 55%, var(--pool-bottom) 0%, var(--pool-top) 70%);
  }
  .brand-plate {
    position: absolute;
    left: 50%;
    top: 50%;
    transform: translate(-50%, -50%);
    width: 400px;
    height: 150px;
    background: var(--paper);
    outline: 2px solid var(--paper);
    outline-offset: 10px;
    display: flex;
    align-items: center;
    justify-content: center;
  }
  .brand-name {
    font-family: "Raleway", sans-serif;
    font-weight: 700;
    color: var(--blue);
    letter-spacing: 2px;
  }
  .brand-plate .brand-name { font-size: 56px; }

  /* Front of card */
  .card-front {
    top: 611px;
    background: linear-gradient(160deg, var(--paper) 30%, var(--paper-shade) 100%);
  }
  .wave { position: absolute; inset: 0; }
  .front-brand {
    position: absolute;
    left: 62px;
    top: 48px;
    font-size: 52px;
  }
  .holder {
    position: absolute;
    left: 62px;
    top: 150px;
  }
  .holder-name {
    margin: 0 0 10px;
    font-family: "Raleway", sans-serif;
    font-weight: 700;
    font-size: 44px;
    color: var(--navy);
    letter-spacing: 0.5px;
  }
  .holder-role, .holder-company {
    margin: 0;
    font-family: "Lato", sans-serif;
    font-size: 25px;
    line-height: 1.35;
    color: var(--ink);
  }
  .address {
    position: absolute;
    left: 62px;
    bottom: 42px;
    margin: 0;
    font-family: "Lato", sans-serif;
    font-style: normal;
    font-size: 25px;
    line-height: 1.45;
    color: var(--paper);
  }
  .contact {
    position: absolute;
    right: 40px;
    top: 225px;
    margin: 0;
    padding: 0;
    list-style: none;
    font-family: "Lato", sans-serif;
    font-size: 24px;
    color: var(--paper);
    text-align: right;
  }
  .contact li {
    display: flex;
    justify-content: flex-end;
    align-items: center;
    gap: 8px;
    line-height: 1.7;
  }
  .contact .sep { opacity: 0.8; }
  .contact svg { width: 20px; height: 20px; fill: var(--paper); }
</style>
</head>
<body>
<main class="canvas">

  <section class="card card-back" aria-label="Card back">
    <div class="pool-photo" role="img" aria-label="Photo of a backyard swimming pool with stone paving, tinted deep navy"></div>
    <div class="brand-plate">
      <span class="brand-name">BRISBANE</span>
    </div>
  </section>

  <section class="card card-front" aria-label="Card front">
    <svg class="wave" viewBox="0 0 960 549" preserveAspectRatio="none" aria-hidden="true">
      <path d="M0,392 C240,388 430,350 545,255 C640,175 720,100 960,92 L960,549 L0,549 Z" fill="var(--blue-deep)"/>
      <path d="M0,408 C250,404 445,368 560,272 C655,192 735,118 960,110 L960,549 L0,549 Z" fill="var(--blue)"/>
    </svg>

    <span class="brand-name front-brand">BRISBANE</span>

    <div class="holder">
      <h1 class="holder-name">DALTON R. WHITFIELD</h1>
      <p class="holder-role">Manager of Legal &amp; Finance</p>
      <p class="holder-company">K.L. Brisbane, Incorporated</p>
    </div>

    <ul class="contact">
      <li>(215) 555-0173 <span class="sep">|</span>
        <svg viewBox="0 0 20 20" aria-label="Mobile"><path d="M6 1h8a1.5 1.5 0 0 1 1.5 1.5v15A1.5 1.5 0 0 1 14 19H6a1.5 1.5 0 0 1-1.5-1.5v-15A1.5 1.5 0 0 1 6 1zm0.5 2v12h7V3zm3.5 13a1 1 0 1 0 0 2 1 1 0 0 0 0-2z"/></svg>
      </li>
      <li>(215) 555-0148 <span class="sep">|</span>
        <svg viewBox="0 0 20 20" aria-label="Office phone"><path d="M2 7c0-2 3-4 8-4s8 2 8 4v2h-4V7.5c-1-.5-2.5-.8-4-.8s-3 .3-4 .8V9H2zm3 3h10l2 7H3zm5 1.5a2.5 2.5 0 1 0 0 5 2.5 2.5 0 0 0 0-5z"/></svg>
      </li>
      <li>dalton@klbrisbane-example.com <span class="sep">|</span>
        <svg viewBox="0 0 20 20" aria-label="Email"><path d="M2 4h16v12H2zm1.5 1.5v.3L10 10.5l6.5-4.7v-.3zm0 2.2v6.8h13V7.7L10 12.4z"/></svg>
      </li>
    </ul>

    <address class="address">
      4837 Grenway Avenue<br>
      Marlow Heights, PA 19243
    </address>
  </section>

</main>
</body>
</html>
```